Business card, folder, and other items for LMV
Lakemoor Vale Oncology, PLLC business cards and material
Please show us folder designs that will house these documents as well.
Thanks for all the great designs.
After seeing double sided designs above, we would like to utilize this design feature. Please submit double sided designs. Thank you.
Please show designs of folder and stationery as well. Current designs look very nice. Thanks for the submissions.

```html
<!DOCTYPE html>
<html lang="en">
<head>
<meta charset="utf-8">
<title>LMV Business Card</title>
<link href="https://fonts.googleapis.com/css2?family=Arimo:wght@400;700&display=swap" rel="stylesheet">
<style>
  :root {
    --page-bg: #e9e7e3;
    --card-white: #ffffff;
    --brand-blue: #2f62b8;
    --text-white: #ffffff;
    --text-soft: #dbe6f7;
  }
  * { margin: 0; padding: 0; box-sizing: border-box; }
  html, body {
    width: 1200px; height: 780px; overflow: hidden;
    background: var(--page-bg);
    font-family: "Arimo", Arial, sans-serif;
  }
  .canvas {
    width: 1200px; height: 780px;
    display: flex; align-items: center; justify-content: center;
  }
  .business-card {
    position: relative;
    width: 1050px; height: 600px;
    border-radius: 34px;
    background: var(--card-white);
    overflow: hidden;
    box-shadow: 0 10px 30px rgba(0,0,0,0.18);
  }
  .card-wave {
    position: absolute; left: 0; top: 0;
    width: 1050px; height: 600px;
  }
  .brand-name {
    position: absolute; left: 150px; top: 120px;
    font-weight: 700; font-size: 72px; line-height: 1;
    color: var(--brand-blue);
  }
  .holder {
    position: absolute; left: 120px; top: 378px;
    color: var(--text-white);
    display: flex; align-items: baseline; gap: 14px;
  }
  .holder-name { font-weight: 700; font-size: 28px; }
  .holder-slash { font-size: 34px; font-weight: 400; }
  .holder-title { font-size: 20px; color: var(--text-soft); }
  .postal-address {
    position: absolute; left: 180px; top: 440px;
    width: 290px; text-align: right;
    color: var(--text-white); font-size: 22px; line-height: 1.35;
    font-style: normal;
  }
  .column-divider {
    position: absolute; left: 500px; top: 432px;
    width: 2px; height: 118px; background: rgba(255,255,255,0.7);
  }
  .contact-list {
    position: absolute; left: 522px; top: 428px;
    list-style: none; color: var(--text-white); font-size: 22px;
  }
  .contact-item {
    display: flex; align-items: center; gap: 12px; height: 40px;
  }
  .contact-icon { width: 24px; height: 24px; flex: none; }
</style>
</head>
<body>
<main class="canvas">
  <article class="business-card" aria-label="Lakemoor Vale Oncology, PLLC business card">
    <svg class="card-wave" viewBox="0 0 1050 600" aria-hidden="true">
      <defs>
        <linearGradient id="blueBand" x1="0" y1="0" x2="0" y2="1">
          <stop offset="0" stop-color="#4a82d6"/>
          <stop offset="1" stop-color="#1d4795"/>
        </linearGradient>
      </defs>
      <path d="M0 318 C 220 300, 380 355, 560 330 C 760 300, 900 250, 1050 262 L1050 600 L0 600 Z" fill="#b9bcc2"/>
      <path d="M0 338 C 220 320, 380 372, 560 348 C 760 320, 900 272, 1050 284 L1050 600 L0 600 Z" fill="url(#blueBand)"/>
    </svg>

    <p class="brand-name">LMV</p>

    <p class="holder">
      <span class="holder-name">Alan Mercer, M.D., DABR</span>
      <span class="holder-slash">/</span>
      <span class="holder-title">President</span>
    </p>

    <address class="postal-address">
      P.O. Box 2480<br>
      Brookfield,<br>
      KY 40512-2480
    </address>

    <span class="column-divider" aria-hidden="true"></span>

    <ul class="contact-list">
      <li class="contact-item">
        <svg class="contact-icon" viewBox="0 0 24 24" aria-hidden="true">
          <path d="M6.6 3.5l3 3.2-1.8 2.4a12 12 0 0 0 7.1 7.1l2.4-1.8 3.2 3-1.7 2.9C11.6 20 4 12.4 3.7 5.2z" fill="#fff"/>
        </svg>
        <span>1-555-214-7730</span>
      </li>
      <li class="contact-item">
        <svg class="contact-icon" viewBox="0 0 24 24" aria-hidden="true">
          <circle cx="12" cy="12" r="4" fill="none" stroke="#fff" stroke-width="2.4"/>
          <path d="M16 8v5.5a2.5 2.5 0 0 0 5 0V12a9 9 0 1 0-4 7.5" fill="none" stroke="#fff" stroke-width="2.4"/>
        </svg>
        <span>mkherwin@lakemoorvale.com</span>
      </li>
      <li class="contact-item">
        <svg class="contact-icon" viewBox="0 0 24 24" aria-hidden="true">
          <circle cx="12" cy="12" r="9" fill="none" stroke="#fff" stroke-width="2"/>
          <ellipse cx="12" cy="12" rx="4" ry="9" fill="none" stroke="#fff" stroke-width="1.6"/>
          <path d="M3 12h18" stroke="#fff" stroke-width="1.6"/>
        </svg>
        <span>www.lakemoorvale.com</span>
      </li>
    </ul>
  </article>
</main>
</body>
</html>
```